Financial Services Company

We need a wordpress design for an existing company based in Boston called Tolvey Capital. We help private investment firms with their fundraising activities. Our website will be pretty static, with occasional news item updates. We have an existing site at www.tolveycapital-example.com. Our new site will have one additional page and a few text updates. Please use our existing color schema of greens and whites. Our logo is in Constantina font. The color of the font is 0,100,55.

Similar sites:
brindlecapitaladvisors-example.com
http://www.morvanpartnersllc-example.com/
www.quillmont-example.com
www.lumberwick-example.com
rtvgo-example.com

Industry/Entity Type

Investment

Requirements
Must have
• We want to have the page tabs at the top of the site. The front page should include a newsfeed that we can update in wordpress with new information.

```html
<!DOCTYPE html>
<html lang="en">
<head>
<meta charset="utf-8">
<title>Tolvey Capital Securities</title>
<link rel="stylesheet" href="https://fonts.googleapis.com/css2?family=Spectral:wght@500;600&family=Source+Sans+3:wght@400;500&display=swap">
<style>
  :root {
    --brand-green: #00643a;
    --heading-green: #0d6b3c;
    --nav-bg: #c8e89c;
    --nav-text: #0b5f35;
    --button-top: #17924f;
    --button-bottom: #0b6f3a;
    --body-text: #5a5a5a;
    --footer-text: #7d8a6c;
    --white: #ffffff;
  }
  * { box-sizing: border-box; margin: 0; padding: 0; }
  html, body { width: 1200px; height: 1091px; overflow: hidden; background: var(--white); }
  body { position: relative; font-family: "Source Sans 3", sans-serif; }

  .top-rule { position: absolute; left: 0; top: 0; width: 1200px; height: 9px; background: var(--brand-green); }

  .brand { position: absolute; left: 107px; top: 40px; color: var(--brand-green); font-family: "Spectral", serif; font-weight: 500; }
  .brand-name { display: block; font-size: 54px; line-height: 56px; letter-spacing: 2px; }
  .brand-sub { display: block; font-size: 20.5px; line-height: 22px; letter-spacing: 2.2px; margin-left: 2px; }

  .main-nav { position: absolute; left: 107px; top: 144px; width: 982px; height: 52px; background: var(--nav-bg); display: flex; }
  .main-nav a { display: flex; align-items: center; justify-content: center; height: 100%; color: var(--nav-text); text-decoration: none; font-family: "Spectral", serif; font-weight: 500; font-size: 16px; letter-spacing: 0.2px; }
  .main-nav a.is-active { background: linear-gradient(var(--button-top), var(--button-bottom)); color: var(--white); }

  .hero { position: absolute; left: 107px; top: 196px; width: 982px; height: 401px; }
  .hero-image { position: absolute; inset: 0; background: linear-gradient(160deg, #e9e9e9 0%, #bdbdbd 35%, #7a7a7a 65%, #4a4a4a 100%); }
  .hero-quote { position: absolute; left: 27px; top: 300px; color: var(--white); font-family: "Spectral", serif; font-weight: 600; font-size: 31px; line-height: 37px; text-shadow: 0 1px 3px rgba(0,0,0,0.5); }

  .feature { position: absolute; top: 628px; }
  .feature h2 { color: var(--heading-green); font-family: "Spectral", serif; font-weight: 600; font-size: 26.5px; line-height: 31px; }
  .feature p { margin-top: 24px; color: var(--body-text); font-size: 12.6px; line-height: 16px; }
  .feature p + p { margin-top: 16px; }
  .feature-experience { left: 124px; width: 290px; }
  .feature-experience p { width: 250px; }
  .feature-services { left: 477px; width: 280px; }
  .feature-services p { width: 265px; }
  .feature-opportunity { left: 807px; width: 280px; }
  .feature-opportunity p { width: 275px; }

  .button-more { position: absolute; display: flex; align-items: center; justify-content: center; width: 107px; height: 36px; background: linear-gradient(var(--button-top), var(--button-bottom)); color: var(--white); font-size: 15px; font-weight: 500; text-decoration: none; }
  .button-experience { left: 127px; top: 916px; }
  .button-services { left: 477px; top: 855px; }
  .button-opportunity { left: 807px; top: 947px; }

  .site-footer { position: absolute; left: 0; top: 1021px; width: 1200px; height: 70px; background: var(--nav-bg); color: var(--footer-text); font-size: 13.5px; }
  .footer-links { position: absolute; left: 533px; top: 25px; }
  .footer-links a { color: var(--footer-text); text-decoration: none; }
  .footer-links .divider { margin: 0 13px 0 14px; }
  .copyright { position: absolute; left: 793px; top: 25px; }
  .social { position: absolute; top: 18px; width: 28px; height: 28px; border-radius: 4px; }
  .social-one { left: 974px; background: #1c4f9c; }
  .social-two { left: 1015px; background: #3aa8df; }
  .social-three { left: 1055px; background: #f39a2b; }
</style>
</head>
<body>
  <div class="top-rule"></div>

  <header class="brand">
    <span class="brand-name">TOLVEY</span>
    <span class="brand-sub">CAPITAL SECURITIES</span>
  </header>

  <nav class="main-nav">
    <a class="is-active" href="#" style="width:129px">HOME</a>
    <a href="#" style="width:136px">TEAM</a>
    <a href="#" style="width:194px">ASSIGNMENTS</a>
    <a href="#" style="width:148px">NEWS</a>
    <a href="#" style="width:190px">SECONDARIES</a>
    <a href="#" style="width:185px">CONTACT US</a>
  </nav>

  <section class="hero">
    <div class="hero-image" role="img" aria-label="Black and white upward view of modern glass office towers against the sky"></div>
    <p class="hero-quote">“Bringing an Investor Mentality<br>to the Fund Raising Process”</p>
  </section>

  <section class="feature feature-experience">
    <h2>Over Experience<br>Building Private Equity</h2>
    <p>We have over 25 years experience building private equity firms from the inside, and our founders have each had a key role building a top-performing investment firm. We have raised $1.5 billion in commitments from leading investors around the globe. Our heritage as former private equity investment professionals provides us with an investor-focused perspective to fundraising that sets us apart from traditional placement firms.</p>
  </section>
  <a class="button-more button-experience" href="#">Learn more</a>

  <section class="feature feature-services">
    <h2>Placement &amp; Advisory<br>Services</h2>
    <p>Tolvey Capital Advisers (“Tolvey”) provides fund placement and advisory services to private equity and venture capital firms. Tolvey was co-founded by Dale Pemberton and Fred Orlow and is an institutional division of Marlowe Securities Corporation, Member NSRA SIPF.</p>
  </section>
  <a class="button-more button-services" href="#">Learn more</a>

  <section class="feature feature-opportunity">
    <h2>The Investment<br>Opportunity.</h2>
    <p>Amid current market turmoil, we are seeing a new group of leading private equity and venture capital firms emerge. Limited partners are looking for relationships with funds that are better positioned to deliver strong returns in today’s economy.</p>
    <p>Right now, smaller funds with focused strategies and capable teams have unprecedented investment opportunities. Tolvey Capital Advisers is working with a select number of these emerging leaders to raise committed capital.</p>
  </section>
  <a class="button-more button-opportunity" href="#">Learn more</a>

  <footer class="site-footer">
    <div class="footer-links"><a href="#">Privacy Policy</a><span class="divider">|</span><a href="#">Sitemap</a></div>
    <div class="copyright">Copreight 2012</div>
    <span class="social social-one" aria-label="Social link"></span>
    <span class="social social-two" aria-label="Social link"></span>
    <span class="social social-three" aria-label="News feed link"></span>
  </footer>
</body>
</html>
```